Local Flower Farm Needs Business Card Design

I need business cards designed for a flower farm based in Eudora, Kansas.
Business Info:
We are a local cut flower farm located in Eudora, Kansas, founded by Darla Hoffstrom. What started as a passion for agriculture and search for more joy in daily life has blossomed into a small business dedicated to providing the community with beautiful, fresh, and sustainable flowers. We specialize in local, seasonal blooms, ensuring that every petal reflects the care and dedication we pour into our craft. Our mission is to deliver the highest quality flowers directly to our customers through local farmers markets and to florists who share our commitment to sustainability. Join us in celebrating the beauty of nature, one bloom at a time!
Contact Details:
Darla Hoffstrom
Owner
Phone 913-555-0147
Facebook: Lorabelle Quinn Blossoms
Instagram: @LorabelleQuinnBlossoms
Website: LorabelleQuinnBlossoms.example
Target Market(s)
Wholesale to Florists and Direct to Consumer via Farmers Market
Industry/Entity Type
Florist, Farm
Contact Information for Business Card
Name, Contact Info, Logo
Look and feel

```html
<!DOCTYPE html>
<html lang="en">
<head>
<meta charset="utf-8">
<title>Lorabelle Quinn Blossoms – Business Card</title>
<link rel="stylesheet" href="https://fonts.googleapis.com/css2?family=Playfair+Display:wght@400;700&family=Poppins:wght@300;400&display=swap">
<style>
  :root {
    --teal-deep: #0b2a2e;
    --paper: #ffffff;
    --backdrop: #e6e7e6;
    --ink-soft: #4a4f51;
    --ink-muted: #8a8e90;
    --ring: rgba(255,255,255,0.85);
  }
  * { box-sizing: border-box; margin: 0; padding: 0; }
  html, body { width: 1200px; height: 874px; overflow: hidden; }
  body {
    background: var(--backdrop);
    font-family: "Poppins", sans-serif;
    position: relative;
  }
  .card {
    position: absolute;
    left: 250px;
    width: 700px;
    height: 400px;
    box-shadow: 0 6px 18px rgba(0,0,0,0.18);
  }
  .card--front { top: 27px; background: var(--teal-deep); }
  .card--back { top: 447px; background: var(--paper); }

  .seal {
    position: absolute;
    left: 50%; top: 50%;
    width: 236px; height: 236px;
    transform: translate(-50%, -50%);
    border: 1.5px solid var(--ring);
    border-radius: 50%;
    display: flex;
    align-items: center;
    justify-content: center;
    text-align: center;
  }
  .seal__name {
    font-family: "Playfair Display", serif;
    font-weight: 400;
    color: var(--paper);
    font-size: 22px;
    line-height: 1.3;
    letter-spacing: 2px;
    text-transform: uppercase;
  }

  .brand-mark {
    position: absolute;
    left: 36px; top: 40px;
    width: 250px; height: 320px;
    display: flex;
    flex-direction: column;
    justify-content: center;
    font-family: "Playfair Display", serif;
    font-weight: 700;
    color: var(--teal-deep);
    font-size: 58px;
    line-height: 1.05;
  }

  .contact {
    position: absolute;
    left: 330px; top: 120px;
    color: var(--ink-soft);
  }
  .contact__name {
    font-family: "Playfair Display", serif;
    font-weight: 700;
    color: var(--teal-deep);
    font-size: 30px;
    line-height: 1.1;
  }
  .contact__role {
    font-size: 13px;
    font-weight: 300;
    color: var(--ink-muted);
    margin-bottom: 26px;
  }
  .contact__list { list-style: none; }
  .contact__item {
    display: flex;
    align-items: center;
    gap: 12px;
    font-size: 15px;
    font-weight: 300;
    line-height: 1.75;
  }
  .contact__icon { width: 14px; height: 14px; flex: none; fill: var(--teal-deep); }
  .contact__social {
    display: flex;
    align-items: center;
    gap: 12px;
    margin-top: 18px;
    font-size: 15px;
    font-weight: 300;
  }
  .contact__dot {
    width: 22px; height: 22px;
    border-radius: 50%;
    background: var(--teal-deep);
    flex: none;
  }
</style>
</head>
<body>
  <section class="card card--front">
    <div class="seal">
      <p class="seal__name">Lorabelle<br>Quinn<br>Blossoms</p>
    </div>
  </section>

  <section class="card card--back">
    <div class="brand-mark">
      <span>Lorabelle</span>
      <span>Quinn</span>
      <span>Blossoms</span>
    </div>

    <div class="contact">
      <h1 class="contact__name">Darla Hoffstrom</h1>
      <p class="contact__role">Owner</p>
      <ul class="contact__list">
        <li class="contact__item">
          <svg class="contact__icon" viewBox="0 0 24 24" aria-hidden="true"><path d="M6.6 10.8a15.1 15.1 0 0 0 6.6 6.6l2.2-2.2a1 1 0 0 1 1-.25 11.4 11.4 0 0 0 3.6.57 1 1 0 0 1 1 1V20a1 1 0 0 1-1 1A17 17 0 0 1 3 4a1 1 0 0 1 1-1h3.5a1 1 0 0 1 1 1c0 1.25.2 2.46.57 3.6a1 1 0 0 1-.25 1z"/></svg>
          913-555-0147
        </li>
        <li class="contact__item">
          <svg class="contact__icon" viewBox="0 0 24 24" aria-hidden="true"><path d="M2 5h20v14H2zm2 2v.5l8 5 8-5V7zm0 2.8V17h16V9.8l-8 5z"/></svg>
          info@LorabelleQuinnBlossoms.example
        </li>
        <li class="contact__item">
          <svg class="contact__icon" viewBox="0 0 24 24" aria-hidden="true"><path d="M12 2a10 10 0 1 0 0 20 10 10 0 0 0 0-20zm6.9 9h-3a15 15 0 0 0-1.3-5.6A8 8 0 0 1 18.9 11zM12 4.1c.9 1.3 1.8 3.6 2 6.9h-4c.2-3.3 1.1-5.6 2-6.9zM9.4 5.4A15 15 0 0 0 8.1 11h-3a8 8 0 0 1 4.3-5.6zM5.1 13h3a15 15 0 0 0 1.3 5.6A8 8 0 0 1 5.1 13zm6.9 6.9c-.9-1.3-1.8-3.6-2-6.9h4c-.2 3.3-1.1 5.6-2 6.9zm2.6-1.3a15 15 0 0 0 1.3-5.6h3a8 8 0 0 1-4.3 5.6z"/></svg>
          www.LorabelleQuinnBlossoms.example
        </li>
      </ul>
      <p class="contact__social">
        <span class="contact__dot" aria-hidden="true"></span>
        @LorabelleQuinnBlossoms
      </p>
    </div>
  </section>
</body>
</html>
```